Visitenkartenerstellung für Dorvek-Estates
Zielgruppe
Männer und Frauen, junge Familien bis hin zum Senior.
Verkauf von hochwertigen Immobilien in Spanien.
Aufgabenstellung
Auf Grund unserer Namensänderung benötigen wir ein neues Visitenkartendesign.
Wir sind eine skandinavische Agentur für Luxus-Immobilien auf Mallorca.
Das Design sollte dementsprechend edel aber dennoch schlicht gestaltet sein!

```html
<!DOCTYPE html>
<html lang="de">
<head>
<meta charset="utf-8">
<title>Dorvek-Estates – Visitenkarte</title>
<link href="https://fonts.googleapis.com/css2?family=Jost:wght@300;400;600&display=swap" rel="stylesheet">
<style>
  :root {
    --ink: #24507b;
    --paper: #ffffff;
    --stage: #ffffff;
    --shadow: rgba(0, 0, 0, 0.18);
  }
  * { margin: 0; padding: 0; box-sizing: border-box; }
  html, body {
    width: 1200px;
    height: 687px;
    overflow: hidden;
    background: var(--stage);
    font-family: "Jost", sans-serif;
    color: var(--ink);
  }
  .stage {
    position: relative;
    width: 1200px;
    height: 687px;
  }
  .card {
    position: absolute;
    top: 172px;
    width: 529px;
    height: 341px;
    background: var(--paper);
    box-shadow: 3px 4px 8px var(--shadow);
  }
  .card--front { left: 53px; }
  .card--back { left: 618px; }

  .brand {
    position: absolute;
    left: 0;
    right: 0;
    top: 104px;
    text-align: center;
  }
  .brand__name {
    font-weight: 400;
    font-size: 58px;
    line-height: 1;
    letter-spacing: 0.5px;
  }
  .brand__tagline {
    margin-top: 12px;
    font-weight: 300;
    font-size: 16.5px;
    letter-spacing: 1px;
    text-transform: uppercase;
  }

  .contact {
    position: absolute;
    left: 27px;
    top: 125px;
    font-weight: 300;
    font-size: 17.5px;
    line-height: 21px;
    text-transform: uppercase;
  }
  .contact__headline {
    font-size: 21px;
    line-height: 24px;
    margin-bottom: 19px;
  }
  .contact__name {
    font-weight: 600;
    letter-spacing: 0.6px;
  }
  .contact__role { font-weight: 300; letter-spacing: 0.3px; }
  .contact__address { margin-bottom: 21px; }
  .contact__address p, .contact__reach p { white-space: nowrap; }
</style>
</head>
<body>
  <main class="stage">
    <section class="card card--front" aria-label="Vorderseite">
      <div class="brand">
        <h1 class="brand__name">Dorvek-Estates</h1>
        <p class="brand__tagline">Luxury Real Estate Mallorca &amp; Ibiza</p>
      </div>
    </section>

    <section class="card card--back" aria-label="Rückseite">
      <div class="contact">
        <h2 class="contact__headline">
          <span class="contact__name">Karin Lindqvist</span>
          <span class="contact__role">Property Manager</span>
        </h2>
        <address class="contact__address">
          <p>C. Mar Blau 12</p>
          <p>07180 Port Nou Spain</p>
        </address>
        <div class="contact__reach">
          <p>Tel. 971555018</p>
          <p>Mobil 0034 60055512</p>
          <p>karin.lindqvist@dorvek-estates.com</p>
          <p>www.dorvek-estates.se</p>
        </div>
      </div>
    </section>
  </main>
</body>
</html>
```